ad for food show brochure

Need to clean up this concept sketch. We are selling food at a festival but the concept isn't quite named. We're looking to create a buzz and have people sign up to be kept apprised of the progress of the chain ... or the first store. The website at the bottom is just for filler, we can add that before ad goes to print. We're not married to this text so if you come up with something better, great. also may want to have a blank @ line for twitter feed and another line for FB page.
The concept is for a Vegan Fast Food place but I need to focus more on the middle of the road diners, we'll get the vegans to come and staunch carnivores won't ever come so it's the middle of the road folks we're after. The slant and speed lines were my attempt to show speed.
Thanks.
This ad is a 5/5 x 2.125 space in the festival brochure. Need this asap.
I also think this needs to be b&w so lets go with that. Just found out COLOR is ok.
That last word in the sketch is not whose but WHERE?
The last word is WHERE not whose. Thanks
We either need to add the word Vegan in the top of the ad or add it in the sentence about all that is vegan and good in the worl.
The ad can be in color. Just to clarify, the word Vegan should be o e of the questions on top. Eithe as part of another question ... 'Vegan fast food?' Or as its own line or bubble.
- pdf file so I can change the website address.

```html
<!DOCTYPE html>
<html lang="en">
<head>
<meta charset="utf-8">
<title>Vegan Fast Food – Coming Soon</title>
<link href="https://fonts.googleapis.com/css2?family=Fjalla+One&family=Quicksand:wght@300;700&family=Chewy&display=swap" rel="stylesheet">
<style>
  :root {
    --burlap: #dccaa6;
    --burlap-deep: #cdb68c;
    --leaf: #7dc243;
    --leaf-dark: #4f8a2f;
    --leaf-light: #a9d66f;
    --bark: #b5812f;
    --white: #ffffff;
  }
  html, body {
    margin: 0;
    padding: 0;
    overflow: hidden;
  }
  .ad {
    position: relative;
    width: 1200px;
    height: 3103px;
    background: var(--burlap);
    overflow: hidden;
  }
  .veg-icons {
    position: absolute;
    left: 40px;
    top: 26px;
    width: 1120px;
    height: 345px;
    background: linear-gradient(180deg, var(--burlap) 0%, var(--burlap-deep) 50%, var(--burlap) 100%);
    border-radius: 24px;
  }
  .questions {
    position: absolute;
    left: 0;
    top: 388px;
    width: 1200px;
    height: 1107px;
    background: var(--leaf);
    color: var(--white);
    font-family: "Fjalla One", "Arial Narrow", sans-serif;
    text-transform: uppercase;
    text-align: center;
  }
  .questions p {
    position: absolute;
    left: 0;
    width: 1200px;
    margin: 0;
    line-height: 1;
    white-space: nowrap;
  }
  .q-big { font-size: 218px; letter-spacing: 2px; }
  .q-small { font-size: 118px; letter-spacing: 1px; }
  .q-line1 { top: 60px; }
  .q-line2 { top: 290px; }
  .q-line3 { top: 540px; }
  .q-line4 { top: 690px; }

  .plea {
    position: absolute;
    left: 0;
    top: 1525px;
    width: 1200px;
    margin: 0;
    text-align: center;
    font-family: "Quicksand", sans-serif;
    font-weight: 700;
    font-size: 140px;
    line-height: 162px;
    color: var(--leaf-dark);
    letter-spacing: -2px;
  }
  .where {
    position: absolute;
    left: 0;
    top: 2070px;
    width: 1200px;
    margin: 0;
    text-align: center;
    font-family: "Chewy", cursive;
    font-size: 250px;
    line-height: 1;
    letter-spacing: 14px;
    color: var(--leaf-light);
    -webkit-text-stroke: 8px var(--leaf-dark);
    paint-order: stroke fill;
  }
  .web-band {
    position: absolute;
    left: 0;
    top: 2353px;
    width: 1200px;
    height: 168px;
    background: var(--bark);
    color: var(--white);
    display: flex;
    align-items: center;
    justify-content: center;
    font-family: "Quicksand", sans-serif;
    font-weight: 700;
    font-size: 70px;
    letter-spacing: 1px;
  }
  .until {
    position: absolute;
    left: 40px;
    top: 2560px;
    color: var(--leaf-dark);
    margin: 0;
  }
  .until-head {
    display: block;
    font-family: "Fjalla One", "Arial Narrow", sans-serif;
    font-size: 160px;
    line-height: 1;
    text-transform: uppercase;
    letter-spacing: 2px;
  }
  .until-body {
    display: block;
    font-family: "Quicksand", sans-serif;
    font-weight: 300;
    font-size: 104px;
    line-height: 128px;
    margin-top: 6px;
  }
  .until-body strong {
    font-weight: 700;
    text-transform: uppercase;
  }
  .drumstick {
    position: absolute;
    left: 935px;
    top: 2550px;
    width: 245px;
    height: 480px;
    background: linear-gradient(200deg, var(--burlap-deep) 0%, #c99a55 60%, var(--leaf-light) 100%);
    border-radius: 120px 120px 40px 40px;
  }
</style>
</head>
<body>
  <main class="ad">
    <div class="veg-icons" role="img" aria-label="Line drawings of a beet, a carrot, an eggplant and an ear of corn in green"></div>

    <section class="questions">
      <p class="q-big q-line1">Vegan Fast</p>
      <p class="q-big q-line2">Food? Yep!</p>
      <p class="q-small q-line3">Coming Soon? Yep!</p>
      <p class="q-big q-line4">In NYC? Yep!</p>
    </section>

    <p class="plea">In the name of<br>all that is good<br>in the World...</p>
    <p class="where">WHERE?</p>

    <div class="web-band">WWW.QUICKLEAF-EATS.COM</div>

    <p class="until">
      <span class="until-head">Until Then...</span>
      <span class="until-body">Enjoy our vegan<br><strong>Leafstix</strong> today!</span>
    </p>
    <div class="drumstick" role="img" aria-label="Line drawing of a drumstick with a green leaf at its tip"></div>
  </main>
</body>
</html>
```